Info Graphic for Radiant Summit Academy

WELCOME To The Radiant Summit Academy (RSA)

We are wanting to create a visual info graphic display of a newly designed transformational pathway program.

Please display the following heading:

The Radiant Summit Academy (RSA) Pathway Program

Subheading:

“Feeling alive and living the life you want to be living.”

Please display each step along the path clearly and with visuals representations that reflect the energy of the word and achievement accomplished.

We would like to display each step individually whilst tying to capture a flow of progression whilst maintaining the look and feel of each step.

The infographic design wants to really spark people’s attention, create impact and a curiosity resulting in a desire to seek more information regarding the program.

Energetic vibrant colours and flow are a must.

A sense of Playfulness, fun and energy is what we are looking for with this design.

The pathway is progressive with each step building on the last and I would like this to be represented in a linear fashion and NOT show steps as hierarchical.

The below documents the steps in order of progression and describes the key focus and outcome for each of the steps.

THE RSA PATHWAY:

Step 1: Wondering Self - Discover the path to transformation and igniting your relationships and life.

Step 2: Quickening Self - Introduction to the Foundational principles.

Step 3: Opening Self - Creating juicy, deep connections with self and others.

Step 4: Reshaping Self - Feeling alive and creating a life of clarity and flow.

Step 5: Blazing Self - Discovering that “This S**T Works” by living the life you want to be living.

Additional Modules available at Reshaping Self (by invitation)

Additional Step: Sending Self - Learn to share the principles and tools to facilitate the RSA Path for family, friends and clients.

Additional Step: Pairing Self - How do couples co-create a relationship that is on fire with passion and expression?

I have attached a previous style guide that we have utilised however don’t want to be limited to just this in the designs.

Happy for this to be utilised and included in designs and we are very open to do something completely different, please be creative.

Any questions or further information required, please let me know.

Target Market(s)

People looking to Feel alive and living the life you want to be living

Industry/Entity Type

Relationship and Personal Development

Requirements
Must have
• Creativity
Nice to have
• Linear display of steps and the explanations at each step included in the description
Should not have
• display hierarchy

```html
<!DOCTYPE html>
<html lang="en">
<head>
<meta charset="utf-8">
<title>The RSA Pathway – Radiant Summit Academy</title>
<link rel="stylesheet" href="https://fonts.googleapis.com/css2?family=Montserrat:wght@600;700;800&family=Open+Sans:wght@400;600&display=swap">
<style>
  :root {
    --violet: #7718e0;
    --violet-deep: #6a12cf;
    --lavender: #dcc8f6;
    --lavender-soft: #e6d7fa;
    --step1: #b685f1;
    --step2: #1640c4;
    --step3: #0bb9e2;
    --step4: #1b8ce8;
    --step5: #ffc846;
    --grey-line: #c4c4c8;
    --grey-arrow: #7d7d7f;
    --ink: #1d1d22;
    --white: #ffffff;
  }
  * { box-sizing: border-box; margin: 0; padding: 0; }
  html, body { width: 1200px; height: 675px; overflow: hidden; background: var(--white); }
  .canvas { position: relative; width: 1200px; height: 675px; overflow: hidden; font-family: "Open Sans", sans-serif; color: var(--ink); }

  .header { position: absolute; inset: 0 0 auto 0; height: 175px; background: var(--lavender); }
  .header-band { position: absolute; left: 0; top: 0; }
  .headline { position: absolute; left: 60px; top: 38px; width: 620px; text-align: center; color: var(--white); font-family: "Montserrat", sans-serif; font-weight: 800; }
  .headline-main { font-size: 30px; line-height: 36px; letter-spacing: 0.3px; }
  .headline-sub { font-size: 24px; line-height: 32px; margin-top: 2px; letter-spacing: 0.4px; }
  .brand { position: absolute; left: 830px; top: 58px; display: flex; align-items: center; gap: 14px; }
  .brand-dot { width: 18px; height: 18px; border-radius: 50%; background: var(--violet); }
  .brand-name { font-family: "Montserrat", sans-serif; font-weight: 700; font-size: 28px; line-height: 32px; color: var(--ink); width: 280px; }

  .pathway-title { position: absolute; left: 0; width: 1200px; top: 202px; text-align: center; font-family: "Montserrat", sans-serif; font-weight: 800; font-size: 34px; letter-spacing: 4px; color: var(--violet); }
  .pathway-art { position: absolute; left: 0; top: 0; }

  .step-label { position: absolute; top: 480px; width: 178px; text-align: center; font-family: "Montserrat", sans-serif; font-weight: 700; font-size: 18px; line-height: 24px; letter-spacing: 0.3px; }
  .step-text { position: absolute; top: 537px; width: 150px; text-align: center; font-size: 11.5px; line-height: 15px; color: var(--ink); }

  .footer { position: absolute; left: 0; top: 619px; width: 1200px; height: 56px; }
  .footer-band { position: absolute; left: 0; top: 0; }
  .footer-lead { position: absolute; left: 50px; top: 17px; font-family: "Montserrat", sans-serif; font-weight: 700; font-size: 19px; color: var(--white); letter-spacing: 0.3px; }
  .module { position: absolute; top: 10px; font-size: 11.5px; line-height: 16px; }
  .module strong { font-weight: 600; }
  .module-sending { left: 318px; width: 410px; color: var(--ink); }
  .module-pairing { left: 793px; width: 380px; color: var(--white); }
</style>
</head>
<body>
<div class="canvas">

  <header class="header">
    <svg class="header-band" width="1200" height="175" viewBox="0 0 1200 175" aria-hidden="true">
      <polygon points="0,0 773,0 689,88 773,175 0,175" fill="var(--violet)"/>
    </svg>
    <div class="headline">
      <p class="headline-main">FEEL ALIVE AND DISCOVER THE LIFE YOU WANT TO LIVE.</p>
      <p class="headline-sub">AWAKEN - WONDER - CONNECT</p>
    </div>
    <div class="brand">
      <span class="brand-dot"></span>
      <span class="brand-name">Radiant Summit Academy</span>
    </div>
  </header>

  <h1 class="pathway-title">THE RSA PATHWAY</h1>

  <svg class="pathway-art" width="1200" height="619" viewBox="0 0 1200 619" aria-hidden="true">
    <!-- loop track -->
    <g fill="none" stroke="var(--grey-line)" stroke-width="6" stroke-linecap="round">
      <path d="M383,222 H190 A100,100 0 0 0 90,322 V338 A100,100 0 0 0 190,438 H206"/>
      <path d="M822,222 H1020 A100,100 0 0 1 1120,322 V338 A100,100 0 0 1 1020,438 H958"/>
      <line x1="250" y1="438" x2="385" y2="438"/>
      <line x1="428" y1="438" x2="563" y2="438"/>
      <line x1="606" y1="438" x2="741" y2="438"/>
      <line x1="784" y1="438" x2="920" y2="438"/>
      <polyline points="78,320 90,334 102,320"/>
      <polyline points="1108,340 1120,326 1132,340"/>
    </g>

    <!-- step bar -->
    <path d="M176,287 H314 V372 H176 A42.5,42.5 0 0 1 176,287 Z" fill="var(--step1)"/>
    <rect x="314" y="287" width="178" height="85" fill="var(--step2)"/>
    <rect x="492" y="287" width="178" height="85" fill="var(--step3)"/>
    <rect x="670" y="287" width="178" height="85" fill="var(--step4)"/>
    <polygon points="848,287 998,287 998,253 1062,330 998,408 998,372 848,372" fill="var(--step5)"/>

    <!-- icons -->
    <g fill="none" stroke="var(--white)" stroke-width="2.4" stroke-linecap="round" stroke-linejoin="round">
      <!-- bulb -->
      <circle cx="225" cy="314" r="11"/>
      <path d="M219,325 V332 H231 V325"/>
      <line x1="220" y1="337" x2="230" y2="337"/>
      <path d="M208,344 Q225,338 242,344"/>
      <line x1="206" y1="302" x2="210" y2="305"/>
      <line x1="244" y1="302" x2="240" y2="305"/>
      <line x1="225" y1="296" x2="225" y2="299"/>
      <!-- bolt in ring -->
      <circle cx="403" cy="329" r="22" stroke-dasharray="4 6"/>
      <polygon points="406,315 395,332 403,332 399,344 412,326 404,326" fill="var(--white)" stroke="none"/>
      <!-- eye -->
      <path d="M556,329 Q581,306 606,329 Q581,352 556,329 Z"/>
      <circle cx="581" cy="329" r="8"/>
      <line x1="544" y1="329" x2="550" y2="329"/>
      <line x1="612" y1="329" x2="618" y2="329"/>
      <line x1="566" y1="308" x2="569" y2="313"/>
      <line x1="596" y1="308" x2="593" y2="313"/>
      <line x1="581" y1="303" x2="581" y2="309"/>
      <!-- gear -->
      <circle cx="765" cy="329" r="16"/>
      <circle cx="765" cy="329" r="7"/>
      <path d="M765,309 V313 M765,345 V349 M745,329 H749 M781,329 H785 M751,315 L754,318 M776,340 L779,343 M779,315 L776,318 M754,340 L751,343"/>
      <line x1="733" y1="322" x2="745" y2="322"/>
      <line x1="733" y1="336" x2="745" y2="336"/>
      <!-- flame -->
      <path d="M938,344 C928,344 925,334 930,326 C932,332 935,332 936,328 C936,320 940,316 944,312 C943,320 950,324 948,334 C947,340 943,344 938,344 Z"/>
    </g>

    <!-- connectors up to bar -->
    <g stroke-width="4" fill="none" stroke-linecap="round" stroke-linejoin="round">
      <g stroke="var(--step1)"><line x1="225" y1="405" x2="225" y2="378"/><polyline points="216,386 225,377 234,386"/></g>
      <g stroke="var(--step2)"><line x1="403" y1="405" x2="403" y2="378"/><polyline points="394,386 403,377 412,386"/></g>
      <g stroke="var(--step3)"><line x1="581" y1="405" x2="581" y2="378"/><polyline points="572,386 581,377 590,386"/></g>
      <g stroke="var(--step4)"><line x1="759" y1="405" x2="759" y2="378"/><polyline points="750,386 759,377 768,386"/></g>
      <g stroke="var(--step5)"><line x1="938" y1="405" x2="938" y2="390"/><polyline points="929,398 938,389 947,398"/></g>
    </g>

    <!-- progress arrows -->
    <g stroke="var(--grey-arrow)" stroke-width="9" fill="none" stroke-linejoin="round">
      <line x1="256" y1="438" x2="304" y2="438"/>
      <line x1="434" y1="438" x2="482" y2="438"/>
      <line x1="612" y1="438" x2="660" y2="438"/>
      <line x1="790" y1="438" x2="838" y2="438"/>
    </g>
    <g stroke="var(--grey-arrow)" stroke-width="5" fill="none" stroke-linecap="round" stroke-linejoin="round">
      <polyline points="298,426 312,438 298,450"/>
      <polyline points="476,426 490,438 476,450"/>
      <polyline points="654,426 668,438 654,450"/>
      <polyline points="832,426 846,438 832,450"/>
    </g>

    <!-- numbered nodes -->
    <g font-family="Montserrat, sans-serif" font-weight="700" font-size="24" fill="var(--white)" text-anchor="middle">
      <circle cx="225" cy="438" r="26" fill="var(--step1)"/><text x="225" y="447">1</text>
      <circle cx="403" cy="438" r="26" fill="var(--step2)"/><text x="403" y="447">2</text>
      <circle cx="581" cy="438" r="26" fill="var(--step3)"/><text x="581" y="447">3</text>
      <circle cx="759" cy="438" r="26" fill="var(--step4)"/><text x="759" y="447">4</text>
      <circle cx="938" cy="438" r="26" fill="var(--step5)"/><text x="938" y="447">5</text>
    </g>
  </svg>

  <h2 class="step-label" style="left:136px;color:var(--step1)">WONDERING<br>SELF</h2>
  <p class="step-text" style="left:150px">Discover the path to transformation and igniting your relationships and life.</p>

  <h2 class="step-label" style="left:314px;color:var(--step2)">QUICKENING<br>SELF</h2>
  <p class="step-text" style="left:328px">Introduction to the Foundational principles.</p>

  <h2 class="step-label" style="left:492px;color:var(--step3)">OPENING<br>SELF</h2>
  <p class="step-text" style="left:506px">Creating juicy, deep connections with self and others.</p>

  <h2 class="step-label" style="left:670px;color:var(--step4)">RESHAPING<br>SELF</h2>
  <p class="step-text" style="left:684px">Feeling alive and creating a life of clarity and flow.</p>

  <h2 class="step-label" style="left:849px;color:var(--step5)">BLAZING<br>SELF</h2>
  <p class="step-text" style="left:863px">Discovering that “This S**T Works” by living the life you want to be living.</p>

  <footer class="footer">
    <svg class="footer-band" width="1200" height="56" viewBox="0 0 1200 56" aria-hidden="true">
      <rect width="1200" height="56" fill="var(--violet)"/>
      <polygon points="255,0 730,0 760,28 730,56 255,56 283,28" fill="var(--lavender-soft)"/>
      <polygon points="730,0 745,0 775,28 745,56 730,56 760,28" fill="var(--step1)"/>
    </svg>
    <p class="footer-lead">ALSO AVAILABLE:</p>
    <p class="module module-sending"><strong>Sending Self -</strong> Learn to share the principles and tools to facilitate the RSA Path for family, friends and clients.</p>
    <p class="module module-pairing"><strong>Pairing Self -</strong> How do couples co-create a relationship that is on fire with passion and expression?</p>
  </footer>

</div>
</body>
</html>
```